Poly Bag Packaging Motorcycle Cables - Vorenza Brand

Poly Bag Dimensions: 33cm(H) x 24cm(W)
We would like to design a genuine Poly Bag Packaging for motorcycle cables.
Vorenza, is one of the leading companies for manufacturing Motorcycles, located in Egypt. Our company is offering high-quality products, the best in the local market, with very competitive prices.
We have a limited time to get this project done, So we Highly appreciate receiving your designs ASAP.
Target Market(s)
Motorcycle Spare parts Buyers
Colors
Designer to choose colors to be used in the design.
Look and feel

```html
<!DOCTYPE html>
<html lang="en">
<head>
<meta charset="utf-8">
<title>Vorenza Motorcycle Cable Poly Bag</title>
<link rel="stylesheet" href="https://fonts.googleapis.com/css2?family=Audiowide&family=Exo+2:ital,wght@1,700&family=Arimo:wght@400;700&display=swap">
<style>
  :root {
    --backdrop: #c9cacb;
    --bag: #eef0f2;
    --red: #dd2b33;
    --blue: #353c9c;
    --yellow: #f8df3a;
    --white: #ffffff;
    --ink: #4a4a4f;
  }
  * { margin: 0; padding: 0; box-sizing: border-box; }
  html, body { width: 1200px; height: 1200px; overflow: hidden; }
  body { background: var(--backdrop); position: relative; font-family: "Arimo", sans-serif; }

  .poly-bag { position: absolute; left: 241px; top: 70px; width: 720px; height: 1047px; background: var(--bag); overflow: hidden; }
  .poly-bag .swoosh { position: absolute; inset: 0; width: 100%; height: 100%; }

  .color-tab { position: absolute; top: 12px; width: 138px; height: 50px; }
  .color-tab--yellow { left: 24px; background: var(--yellow); }
  .color-tab--red { left: 292px; background: var(--red); }
  .color-tab--blue { left: 561px; background: var(--blue); }

  .title-band { position: absolute; left: 0; top: 160px; width: 720px; height: 105px; background: var(--red); color: var(--white); }
  .title-band__heading { position: absolute; left: 24px; top: 10px; font-family: "Audiowide", sans-serif; font-size: 54px; font-weight: 400; letter-spacing: 1px; line-height: 1.2; white-space: nowrap; }
  .title-band__tagline { position: absolute; left: 20px; top: 68px; font-family: "Exo 2", sans-serif; font-style: italic; font-weight: 700; font-size: 20px; white-space: nowrap; }

  .product-label { position: absolute; left: 196px; top: 587px; width: 330px; height: 170px; border-radius: 16px; overflow: hidden; background: var(--blue); }
  .product-label__brand { height: 62px; background: var(--white); display: flex; align-items: center; justify-content: center; gap: 10px; }
  .product-label__mark { width: 26px; height: 26px; border-radius: 50%; background: var(--ink); }
  .product-label__name { font-family: "Audiowide", sans-serif; font-size: 30px; color: var(--ink); letter-spacing: 2px; }
  .spec-table { margin: 12px auto 0; width: 244px; border-collapse: collapse; color: var(--white); font-size: 15px; }
  .spec-table td { border: 2px solid var(--white); text-align: center; height: 22px; width: 50%; }
  .product-label__origin { text-align: center; color: var(--white); font-size: 10px; margin-top: 8px; }
</style>
</head>
<body>
  <div class="poly-bag">
    <svg class="swoosh" viewBox="0 0 720 1047" aria-hidden="true">
      <path d="M0 553 Q150 850 720 1047 L0 1047 Z" fill="var(--blue)"/>
      <path d="M0 553 Q60 880 330 1047 L0 1047 Z" fill="var(--red)"/>
      <path d="M720 660 Q640 960 446 1047 L720 1047 Z" fill="var(--yellow)"/>
    </svg>

    <div class="color-tab color-tab--yellow"></div>
    <div class="color-tab color-tab--red"></div>
    <div class="color-tab color-tab--blue"></div>

    <div class="title-band">
      <h1 class="title-band__heading">MOTORCYCLE CABLE</h1>
      <p class="title-band__tagline">HIGH QUALITY PRODUCT</p>
    </div>

    <div class="product-label">
      <div class="product-label__brand">
        <span class="product-label__mark"></span>
        <span class="product-label__name">VORENZA</span>
      </div>
      <table class="spec-table">
        <tr><td>ITEM</td><td>BRAKE CABLE</td></tr>
        <tr><td>MODEL</td><td>XYZ 456789</td></tr>
        <tr><td>QTY</td><td>001</td></tr>
      </table>
      <p class="product-label__origin">MADE IN EGYPT</p>
    </div>
  </div>
</body>
</html>
```